Redesign of QuillLexicon.com in Bootstrap 4

Current design of QuillLexicon.com is not responsive. We need to change it to latest version of Bootstrap 4 keeping essential elements in place.

Apart from home page, we need designs for http://www.quilllexicon.com/meaning/cat also.

Coding

Coded - Design and coding required

Number of Pages Required

2 page

Colors
34a7d8

Requirements
Must have
• Bootstrap 4

```html
<!DOCTYPE html>
<html lang="en">
<head>
<meta charset="utf-8">
<title>QuillLexicon.com – Home</title>
<link rel="stylesheet" href="https://fonts.googleapis.com/css2?family=Open+Sans:wght@400;600;700;800&display=swap">
<style>
:root{
  --blue:#34a7d8;
  --blue-deep:#1f8fc4;
  --orange:#f7941d;
  --dark:#333333;
  --ink:#3a3a3a;
  --muted:#666;
  --paper:#f0f0f0;
  --white:#fff;
}
*{margin:0;padding:0;box-sizing:border-box}
html,body{width:864px;height:1200px;overflow:hidden;background:var(--white);font-family:"Open Sans",sans-serif;color:var(--ink)}
.page{position:relative;width:864px;height:1200px}
.abs{position:absolute}
/* header */
.brand{left:116px;top:22px;font-size:14px;font-weight:700;color:var(--dark)}
.brand-dot{display:inline-block;width:9px;height:9px;border-radius:50%;background:var(--orange);margin-right:4px;vertical-align:middle}
.nav{top:29px;font-size:7px;color:#555;letter-spacing:.1px}
.nav.active{color:var(--blue)}
.login{left:656px;top:21px;width:92px;height:27px;border-radius:14px;background:var(--blue);border:2px solid #cfe8f4;color:#fff;font-size:7px;display:flex;align-items:center;justify-content:center}
/* hero */
.hero{left:0;top:65px;width:864px;height:321px;background:var(--blue)}
.search-frame{left:165px;top:83px;width:534px;height:49px;border-radius:4px;background:var(--blue-deep)}
.search-field{left:170px;top:88px;width:524px;height:39px;background:#fff;border-radius:2px}
.search-field span{position:absolute;left:47px;top:12px;font-size:10px;color:#aaa}
.search-btn{left:613px;top:91px;width:79px;height:34px;background:var(--orange);color:#fff;font-size:9px;font-weight:700;display:flex;align-items:center;justify-content:center}
.search-hint{left:170px;top:139px;font-size:7.5px;color:var(--dark)}
.headline{left:0;width:864px;top:176px;text-align:center;font-size:25px;font-weight:700;color:var(--dark)}
.features{left:268px;top:221px;list-style:none}
.features li{height:19.4px;font-size:10px;font-weight:700;color:#fff;display:flex;align-items:center}
.features svg{margin-right:9px}
/* browse */
.browse{left:0;top:386px;width:864px;height:32px;background:var(--dark);color:#fff}
.browse h2{position:absolute;left:131px;top:8px;font-size:12px;font-weight:700}
.letters{position:absolute;left:295px;top:10px;width:438px;display:flex;justify-content:space-between;font-size:9px;font-weight:700}
.letters .on{color:var(--orange)}
/* word of day */
.daily{left:0;top:418px;width:864px;height:182px;background:var(--paper)}
.rule{height:1px;background:var(--dark)}
.label{font-size:15px;font-weight:700;line-height:20px;color:var(--dark)}
.term{font-size:14px;font-weight:600;color:#555}
.body{font-size:7.6px;line-height:13px;color:var(--muted)}
.more{font-size:7.5px;font-weight:700;color:var(--blue)}
.share{font-size:7.5px;color:var(--muted);display:flex;align-items:center;gap:4px}
.share i{display:block;width:12px;height:12px;border:1px solid #ccc;background:#fff}
.share i.fill{background:var(--blue);border-color:var(--blue)}
.divider{left:430px;top:430px;width:1px;height:150px;background:#ddd}
/* cards */
.shot{width:199px;height:120px}
.card-title{font-size:13px;font-weight:700;color:var(--dark)}
.card-text{font-size:7.6px;line-height:13px;color:var(--muted)}
.btn{height:23px;border:1px solid var(--blue);color:var(--blue);font-size:7.5px;font-weight:700;display:flex;align-items:center;justify-content:center}
.btn.solid{background:var(--blue);color:#fff}
/* newsletter */
.news{left:0;top:944px;width:864px;height:78px;background:var(--dark);color:#fff}
.news h3{position:absolute;left:117px;top:24px;font-size:10px;font-weight:700}
.news p{position:absolute;left:117px;top:42px;font-size:7.5px}
.email{left:333px;top:968px;width:307px;height:27px;background:#fff;font-size:7.5px;color:#777;padding:8px 9px}
.subscribe{left:656px;top:968px;width:92px;height:27px;background:var(--orange);color:#fff;font-size:7px;font-weight:700;display:flex;align-items:center;justify-content:center}
/* footer */
.footer{left:0;top:1022px;width:864px;height:136px;background:var(--blue)}
.foot-brand{left:125px;top:1078px;font-size:14px;font-weight:700;color:var(--dark)}
.col h4{font-size:9.5px;font-weight:700;color:#fff;margin-bottom:9px}
.col a{display:block;font-size:7.6px;color:#fff;text-decoration:none;margin-bottom:10px}
.copy{left:116px;top:1173px;font-size:7.5px;color:#aaa}
.social{left:697px;top:1174px;display:flex;gap:9px}
.social i{display:block;width:9px;height:9px;border-radius:50%;background:#bbb}
.social i.first{background:var(--blue)}
</style>
</head>
<body>
<div class="page">
  <header>
    <div class="abs brand"><span class="brand-dot"></span>QuillLexicon</div>
    <nav>
      <span class="abs nav active" style="left:322px">HOME</span>
      <span class="abs nav" style="left:366px">IDIOMS</span>
      <span class="abs nav" style="left:414px">COMMON ERRORS</span>
      <span class="abs nav" style="left:500px">CROSSWORD</span>
      <span class="abs nav" style="left:565px">BLOG</span>
      <span class="abs nav" style="left:601px">CONTACT</span>
    </nav>
    <div class="abs login">LOGIN / REGISTER</div>
  </header>

  <section class="abs hero" role="img" aria-label="Blue banner with faint scattered adjective words in the background"></section>
  <div class="abs search-frame"></div>
  <div class="abs search-field">
    <svg class="abs" style="left:10px;top:7px" width="24" height="24" viewBox="0 0 24 24"><circle cx="10" cy="10" r="7" fill="none" stroke="#ccc" stroke-width="3"/><line x1="15" y1="15" x2="22" y2="22" stroke="#ccc" stroke-width="3.5" stroke-linecap="round"/></svg>
    <span>Enter a word or phrase</span>
  </div>
  <div class="abs search-btn">SEARCH</div>
  <div class="abs search-hint">(eg. origin, sign, butterfly)</div>
  <h1 class="abs headline">SEARCH, SAVE AND MASTER WORDS</h1>
  <ul class="abs features">
    <li><svg width="10" height="9" viewBox="0 0 10 9"><path d="M1 5l3 3 5-7" fill="none" stroke="#333" stroke-width="2"/></svg>Search from more than 300,000 words and phrases</li>
    <li><svg width="10" height="9" viewBox="0 0 10 9"><path d="M1 5l3 3 5-7" fill="none" stroke="#333" stroke-width="2"/></svg>Multiple usages to clarify the context</li>
    <li><svg width="10" height="9" viewBox="0 0 10 9"><path d="M1 5l3 3 5-7" fill="none" stroke="#333" stroke-width="2"/></svg>Audio, phonetics, meanings, synonyms and antonyms</li>
    <li><svg width="10" height="9" viewBox="0 0 10 9"><path d="M1 5l3 3 5-7" fill="none" stroke="#333" stroke-width="2"/></svg>Save the words to your personal deck and access from anywhere</li>
    <li><svg width="10" height="9" viewBox="0 0 10 9"><path d="M1 5l3 3 5-7" fill="none" stroke="#333" stroke-width="2"/></svg>It’s FREE</li>
  </ul>

  <section class="abs browse">
    <h2>BROWSE DICTIONARY</h2>
    <div class="letters"><span>A</span><span>B</span><span>C</span><span class="on">D</span><span>E</span><span>F</span><span>G</span><span>H</span><span>I</span><span>J</span><span>K</span><span>L</span><span>M</span><span>N</span><span>O</span><span>P</span><span>Q</span><span>R</span><span>S</span><span>T</span><span>U</span><span>V</span><span>W</span><span>X</span><span>Y</span><span>Z</span></div>
  </section>

  <section class="abs daily"></section>
  <div class="abs rule" style="left:116px;top:457px;width:92px"></div>
  <div class="abs label" style="left:127px;top:465px">WORD OF<br>THE DAY</div>
  <div class="abs rule" style="left:116px;top:510px;width:92px"></div>
  <div class="abs share" style="left:126px;top:541px">Share <i class="fill"></i><i></i><i></i></div>
  <div class="abs term" style="left:231px;top:463px">proprietary
    <svg style="vertical-align:middle;margin-left:8px" width="12" height="12" viewBox="0 0 12 12"><circle cx="6" cy="6" r="6" fill="#fff"/><path d="M3 5h2l2-2v6L5 7H3z" fill="var(--orange)"/></svg></div>
  <p class="abs body" style="left:230px;top:488px;width:176px">/prə ˈpraɪ ə ˌtɛ ri / (n) an unincorporated business owned by a single person who is responsible for its liabilities and entitled to its profits</p>
  <div class="abs more" style="left:230px;top:534px">MORE INFO</div>
  <div class="abs divider"></div>
  <div class="abs rule" style="left:440px;top:457px;width:92px"></div>
  <div class="abs label" style="left:454px;top:465px">ENGLISH<br>TIDBIT</div>
  <div class="abs rule" style="left:440px;top:510px;width:92px"></div>
  <div class="abs term" style="left:559px;top:464px">later/latter</div>
  <p class="abs body" style="left:560px;top:488px;width:166px">In a string of things or list, "latter" is the last thing on the list. "Later" is usually in terms of time; "latter-day" is, however, the only exception.</p>

  <div class="abs shot" style="left:116px;top:648px;background:linear-gradient(135deg,#ddd,#555 55%,#222)" role="img" aria-label="Close-up of a crossword puzzle with a pen"></div>
  <div class="abs card-title" style="left:130px;top:785px">DAILY CROSSWORD</div>
  <p class="abs card-text" style="left:131px;top:810px;width:155px">Take this daily crossword challenge from Quill Lexicon.</p>
  <div class="abs btn" style="left:131px;top:865px;width:65px">SOLVE NOW</div>

  <div class="abs shot" style="left:332px;top:648px;background:linear-gradient(180deg,#dfe8f2,#f5f7fa)" role="img" aria-label="Screenshot of the browser addon showing a word definition popup"></div>
  <div class="abs card-title" style="left:344px;top:785px">FLAREFOX ADDON</div>
  <p class="abs card-text" style="left:344px;top:810px;width:175px">Add this tool to your Flarefox and quickly look up for definitions from any website without leaving the page.</p>
  <div class="abs btn solid" style="left:345px;top:865px;width:67px">GET IT NOW</div>

  <div class="abs shot" style="left:548px;top:648px;background:linear-gradient(135deg,#8a8f6a,#3a3a3a 60%,#222)" role="img" aria-label="Hand holding a phone running the dictionary app"></div>
  <div class="abs card-title" style="left:562px;top:785px">DESIGNED FOR HANDSET</div>
  <p class="abs card-text" style="left:562px;top:810px;width:172px">Quill Lexicon is specially designed for your Handset to quickly lookup meaining, usages and audio of words.</p>
  <div class="abs btn" style="left:562px;top:865px;width:89px">DOWNLOAD NOW</div>

  <section class="abs news">
    <h3>NEWSLETTER SUBSCRIPTION</h3>
    <p>Learn a new word every day. Direct into your inbox!</p>
  </section>
  <div class="abs email">Enter your email address</div>
  <div class="abs subscribe">SUBSCRIBE</div>

  <footer class="abs footer"></footer>
  <div class="abs foot-brand">QuillLexicon</div>
  <div class="abs col" style="left:279px;top:1050px"><h4>QuillLexicon.com</h4><a>Faq</a><a>Contact</a><a>Blog</a></div>
  <div class="abs col" style="left:441px;top:1050px"><h4>Others</h4><a>Popular Words</a><a>Common Errors in English</a><a>Test Prep Online</a></div>
  <div class="abs col" style="left:603px;top:1050px"><h4>Legal</h4><a>Privacy Policy</a><a>Terms of Use</a></div>
  <div class="abs copy">© 2016 QuillLexicon.com. All rights reserved.</div>
  <div class="abs social"><i class="first"></i><i></i><i></i></div>
</div>
</body>
</html>
```